Avocado Oil label - upmarket elegant design

We are a distributor of healthy and organic food in a process of adding avocado oil to our selection of products. The oil will be packaged in round Dorica bottles and we are looking for a simple and elegant label design highlighting both culinary and health benefits of avocado oil. The label size should be a one piece square, approx. 5.5 x 5.5 inches (14 x 14 cm). The oil will be sold under brand name Velmoria. Most label designs currently on the market feature some form of the avocado fruit, some have a depiction of oil extracted from the fruit, etc. but we are obviously open to other ideas and don't want to constrain designer's creativity in any way. The label should be designed to wrap around the bottle in one piece. Attached images are for inspiration only

Target Market(s)

Upscale, health conscious consumers

Requirements
Must have
• In addition to graphics:

- Brand name (Velmoria)
- Extra Virgin
- Avocado Oil
- First Cold pressed
- 8.45 oz / 250 ml
- space for bar code with EAN number (will be provided), and approx 0.75" x 1.5" blank space for Batch Number and Best Before date to be printed during bottling
- space for nutritional label (will be provided)
- Ingredients : 100% Pure Extra Virgin Avocado Oil
- "High in vitamin E, heart healthy monounsaturated fats, antioxidants, lutein and beta sitosterol"
- "Non GMO, does not contain trans fats, cholesterol, preservatives or artificial ingredients"
- "High smoke point (500F/260C), perfect for high heat cooking, salads, marinades and baking"
- "Store in a cool dark place"

```html
<!DOCTYPE html>
<html lang="en">
<head>
<meta charset="UTF-8">
<title>Velmoria Avocado Oil – Front Label</title>
<link href="https://fonts.googleapis.com/css2?family=Pinyon+Script&family=Lobster&family=Tenor+Sans&family=Montserrat:wght@300;500&display=swap" rel="stylesheet">
<style>
  :root {
    --page-bg: #ffffff;
    --label-top: #eef2ea;
    --label-light: #b9dc8e;
    --label-mid: #5fa83a;
    --label-deep: #2f8a33;
    --label-bottom: #1c6a2c;
    --brand-ink: #1d2418;
    --text-light: #ffffff;
    --text-soft: #d6e8cf;
    --art-dark: #2b5a22;
    --art-light: #8fbf4a;
    --art-oil: #9a9a2a;
  }
  * { margin: 0; padding: 0; box-sizing: border-box; }
  html, body {
    width: 900px;
    height: 1200px;
    overflow: hidden;
    background: var(--page-bg);
  }
  .canvas {
    position: relative;
    width: 900px;
    height: 1200px;
    background: var(--page-bg);
  }
  .label {
    position: absolute;
    left: 200px;
    top: 16px;
    width: 500px;
    height: 1168px;
    overflow: hidden;
    background: linear-gradient(180deg,
      var(--label-top) 0%,
      var(--label-top) 4%,
      var(--label-light) 18%,
      var(--label-mid) 34%,
      var(--label-deep) 60%,
      var(--label-bottom) 100%);
  }
  .brand {
    position: absolute;
    top: 40px;
    left: 0;
    width: 100%;
    text-align: center;
  }
  .brand-dot {
    display: block;
    width: 150px;
    height: 150px;
    margin: 0 auto 16px;
    border-radius: 50%;
    background: var(--brand-ink);
  }
  .brand-name {
    font-family: "Pinyon Script", cursive;
    font-size: 72px;
    line-height: 1;
    color: var(--brand-ink);
  }
  .hero-art {
    position: absolute;
    top: 300px;
    left: 0;
    width: 500px;
    height: 470px;
  }
  .product-name {
    position: absolute;
    top: 765px;
    left: 0;
    width: 100%;
    text-align: center;
    font-family: "Lobster", cursive;
    font-size: 92px;
    line-height: 1;
    color: var(--text-light);
  }
  .grade {
    position: absolute;
    top: 893px;
    left: 0;
    width: 100%;
    text-align: center;
    font-family: "Tenor Sans", sans-serif;
    font-size: 36px;
    letter-spacing: 1px;
    color: var(--text-light);
  }
  .process {
    position: absolute;
    top: 997px;
    left: 0;
    width: 100%;
    text-align: center;
    font-family: "Montserrat", sans-serif;
    font-weight: 300;
    font-size: 21px;
    letter-spacing: 1.5px;
    color: var(--text-soft);
  }
  .volume {
    position: absolute;
    top: 1092px;
    left: 0;
    width: 100%;
    text-align: center;
    font-family: "Montserrat", sans-serif;
    font-weight: 500;
    font-size: 23px;
    color: var(--text-light);
  }
</style>
</head>
<body>
  <main class="canvas">
    <section class="label">
      <header class="brand">
        <span class="brand-dot"></span>
        <div class="brand-name">Velmoria</div>
      </header>

      <svg class="hero-art" viewBox="0 0 500 470" role="img" aria-label="Illustration of a whole avocado and a halved avocado with its pit, wrapped in a splash of golden-green oil">
        <defs>
          <radialGradient id="heroGlow" cx="50%" cy="55%" r="60%">
            <stop offset="0%" stop-color="var(--art-light)"/>
            <stop offset="55%" stop-color="var(--art-oil)" stop-opacity="0.55"/>
            <stop offset="100%" stop-color="var(--art-dark)" stop-opacity="0"/>
          </radialGradient>
        </defs>
        <rect x="0" y="0" width="500" height="470" fill="url(#heroGlow)"/>
      </svg>

      <h1 class="product-name">Avocado Oil</h1>
      <p class="grade">EXTRA VIRGIN</p>
      <p class="process">First Cold Pressed</p>
      <p class="volume">8.45 oz / 250 ml</p>
    </section>
  </main>
</body>
</html>
```